Werbebanner für Textilreinigung
Zielgruppe
Wir sind eine Textilreinigung mit einem großen Spektrum an Leistungen.
Unsere Zielgruppe sind Privat Personen die ihre Textilien zum reinigen zu uns bringen.
Aufgabenstellung
Es sollen 5 Straßenbanner designt werden. Diese werden bei Ortseinfahrten/- ausfahrten, aufgehängt. Das Design soll modern sein und zu unserem Logo passen. Die Herausforderung bei den Straßenbannern ist die Zielgruppe, die Autofahrer. Der Banner wird beim Vorbeifahren für nur 1-2 Sekunden gesehen. Auf jedem Banner soll ein Sonderangebot mit eingebaut werden. Zu der Zeit in der der Banner aufgehängt ist, erhält der Kunde 20% auf die jeweilige Dienstleistung.
Hier die verschiedenen Banner:
-Betten & Daunenreinigung | -Trachten und Lederreinigung | -Braut & Festtagskleider reinigung |-Teppichwäsche (inkl. kostenlosen Abhol und Lieferservice) |-Hemdenservice
Bannergröße beträgt 100cm(H) x 300cm(B)
Das gilt für alle 5 verschiedenen Banner.
Es soll auf jedem Banner stehen:
-Sonderangebot 20%
-unser Logo (siehe Dateien)
-unsere Adresse
-Telefonnummer
-Aufruf zur Aktion
Anmerkung: Auf der EPS.Datei muss ein kleiner Schriftzug hinzugefügt werden der auf der PDF. zu sehen ist.

```html
<!DOCTYPE html>
<html lang="de">
<head>
<meta charset="utf-8">
<title>Straßenbanner Textilreinigung</title>
<link rel="stylesheet" href="https://fonts.googleapis.com/css2?family=Fira+Sans:wght@600;700;800&family=Fira+Sans+Condensed:wght@700&display=swap">
<style>
  :root {
    --green: #7fb23a;
    --green-dark: #5e8f2a;
    --green-light: #b9cf3a;
    --yellow: #e4e64a;
    --blue: #213f8f;
    --blue-purple: #4a3d98;
    --white: #ffffff;
    --shadow: #56782a;
  }
  * { box-sizing: border-box; margin: 0; padding: 0; }
  html, body { width: 848px; height: 1200px; overflow: hidden; background: var(--white); }
  body { position: relative; font-family: "Fira Sans", sans-serif; }

  .banner {
    position: absolute;
    left: 139px;
    width: 570px;
    height: 190px;
    overflow: hidden;
    background:
      radial-gradient(circle at 45% 2%, rgba(255,255,240,0.95) 0, rgba(255,255,200,0.5) 18px, rgba(255,255,200,0) 45px),
      radial-gradient(ellipse 130px 110px at 40% 22%, rgba(228,230,74,0.75) 0, rgba(200,215,60,0.4) 60%, rgba(200,215,60,0) 100%),
      radial-gradient(ellipse 250px 180px at 30% 30%, rgba(185,207,58,0.5) 0, rgba(185,207,58,0) 100%),
      linear-gradient(90deg, var(--green) 0%, #8bb93d 50%, var(--green) 100%);
  }
  .banner--1 { top: 59px; }
  .banner--2 { top: 282px; }
  .banner--3 { top: 505px; }
  .banner--4 { top: 728px; }
  .banner--5 { top: 951px; }

  .offer-badge {
    position: absolute;
    left: 22px;
    top: 22px;
    width: 190px;
    height: 112px;
    transform: rotate(-5deg);
  }
  .offer-badge__shadow {
    position: absolute;
    inset: 0;
    transform: translate(8px, 9px);
    background: var(--shadow);
    border-radius: 10px;
  }
  .offer-badge__card {
    position: absolute;
    inset: 0;
    background: var(--white);
    border-radius: 10px;
    text-align: center;
    padding-top: 4px;
  }
  .offer-badge__value {
    display: block;
    font-family: "Fira Sans Condensed", sans-serif;
    font-weight: 700;
    font-size: 70px;
    line-height: 70px;
    letter-spacing: -3px;
    background: linear-gradient(120deg, var(--blue) 30%, #7a4fa6 55%, var(--blue-purple) 75%);
    -webkit-background-clip: text;
    background-clip: text;
    color: transparent;
  }
  .offer-badge__label {
    display: block;
    font-family: "Fira Sans Condensed", sans-serif;
    font-weight: 700;
    font-size: 20px;
    line-height: 22px;
    color: var(--blue);
    letter-spacing: -0.3px;
  }

  .service-title {
    position: absolute;
    color: var(--white);
    font-weight: 700;
    line-height: 1;
  }
  .banner--1 .service-title { left: 278px; top: 20px; font-size: 50px; line-height: 44px; }
  .banner--2 .service-title { left: 234px; top: 22px; font-size: 42px; }
  .service-title__note { display: block; font-size: 22px; line-height: 26px; margin-top: 10px; font-weight: 600; }
  .banner--3 .service-title { left: 230px; top: 16px; font-size: 36px; line-height: 40px; }
  .banner--4 .service-title { left: 238px; top: 22px; font-size: 38px; line-height: 42px; }
  .banner--5 .service-title { left: 238px; top: 22px; font-size: 38px; line-height: 42px; }

  .contact-bar {
    position: absolute;
    left: 0;
    top: 152px;
    width: 422px;
    height: 38px;
    background: linear-gradient(90deg, var(--blue) 0%, #2a4799 60%, var(--blue) 100%);
    color: var(--white);
    font-weight: 600;
    font-size: 16px;
    line-height: 38px;
    padding-left: 17px;
    white-space: nowrap;
  }

  .brand-box {
    position: absolute;
    left: 422px;
    top: 122px;
    width: 148px;
    height: 68px;
    background: var(--white);
    border-top-left-radius: 16px;
    display: flex;
    align-items: center;
    gap: 8px;
    padding-left: 12px;
  }
  .brand-box__dot {
    width: 18px;
    height: 18px;
    border-radius: 50%;
    background: var(--green);
    flex: none;
  }
  .brand-box__name {
    font-weight: 700;
    font-size: 18px;
    color: var(--blue);
  }
</style>
</head>
<body>

<section class="banner banner--1">
  <div class="offer-badge"><div class="offer-badge__shadow"></div><div class="offer-badge__card"><span class="offer-badge__value">20%</span><span class="offer-badge__label">SONDERANGEBOT</span></div></div>
  <h2 class="service-title">Hemden-<br>service</h2>
  <div class="contact-bar">86000 Talbach – Mühlenweg 7 – Tel: 01234 - 5678</div>
  <div class="brand-box"><span class="brand-box__dot"></span><span class="brand-box__name">Glanzwerk</span></div>
</section>

<section class="banner banner--2">
  <div class="offer-badge"><div class="offer-badge__shadow"></div><div class="offer-badge__card"><span class="offer-badge__value">20%</span><span class="offer-badge__label">SONDERANGEBOT</span></div></div>
  <h2 class="service-title">Teppichwäsche<span class="service-title__note">inkl. kostenlose Abholung<br>und Lieferung</span></h2>
  <div class="contact-bar">86000 Talbach – Mühlenweg 7 – Tel: 01234 - 5678</div>
  <div class="brand-box"><span class="brand-box__dot"></span><span class="brand-box__name">Glanzwerk</span></div>
</section>

<section class="banner banner--3">
  <div class="offer-badge"><div class="offer-badge__shadow"></div><div class="offer-badge__card"><span class="offer-badge__value">20%</span><span class="offer-badge__label">SONDERANGEBOT</span></div></div>
  <h2 class="service-title">Braut- und<br>Festtagskleidung-<br>Reinigung</h2>
  <div class="contact-bar">86000 Talbach – Mühlenweg 7 – Tel: 01234 - 5678</div>
  <div class="brand-box"><span class="brand-box__dot"></span><span class="brand-box__name">Glanzwerk</span></div>
</section>

<section class="banner banner--4">
  <div class="offer-badge"><div class="offer-badge__shadow"></div><div class="offer-badge__card"><span class="offer-badge__value">20%</span><span class="offer-badge__label">SONDERANGEBOT</span></div></div>
  <h2 class="service-title">Trachten- und<br>Lederreinigung</h2>
  <div class="contact-bar">86000 Talbach – Mühlenweg 7 – Tel: 01234 - 5678</div>
  <div class="brand-box"><span class="brand-box__dot"></span><span class="brand-box__name">Glanzwerk</span></div>
</section>

<section class="banner banner--5">
  <div class="offer-badge"><div class="offer-badge__shadow"></div><div class="offer-badge__card"><span class="offer-badge__value">20%</span><span class="offer-badge__label">SONDERANGEBOT</span></div></div>
  <h2 class="service-title">Betten- und<br>Daunenreinigung</h2>
  <div class="contact-bar">86000 Talbach – Mühlenweg 7 – Tel: 01234 - 5678</div>
  <div class="brand-box"><span class="brand-box__dot"></span><span class="brand-box__name">Glanzwerk</span></div>
</section>

</body>
</html>
```